Letterhead

We need a professional, compelling letterhead that can be used for print and email stationary. We have the logo and the letterhead styling and colors should blend seamlessly and be complimentary. Looking for something unique and thoughtful.
Updates

Reason: There are good ideas and am requesting changes to some ideas in order to make a final decision. Thank you for for submissions. Also, I have uploaded the ai file. Please use that file. Thank you.

If you cannot see the .ai version of the logo that I have tried to upload, please message me if you want to make changes to your submission or submit new design and I will send that file to you directly. This .ai will need to be used in order to ensure high quality printing. Thank you.

Target Market(s)

Clients. Business partners.

Industry/Entity Type

It Professional

Requirements
Must have
• Our logo incorporated. Also the phrase, or tag line - WHERE PROGRESS BEGINS.
Should not have
• Not boring. Not typical. Not too busy.

```html
<!DOCTYPE html>
<html lang="en">
<head>
<meta charset="utf-8">
<title>Meridian Advisory Group — Letterhead</title>
<link rel="stylesheet" href="https://fonts.googleapis.com/css2?family=EB+Garamond:wght@400;500&display=swap">
<style>
  :root {
    --backdrop: #808080;
    --paper: #ffffff;
    --navy: #0e3563;
    --rule-fade: rgba(14, 53, 99, 0);
    --footer-ink: #a3a3a3;
    --footer-band: #e6e6e6;
  }
  * { margin: 0; padding: 0; box-sizing: border-box; }
  html, body { width: 1200px; height: 997px; overflow: hidden; background: var(--backdrop); }
  .canvas { position: relative; width: 1200px; height: 997px; }
  .sheet {
    position: absolute; left: 299px; top: 119px; width: 601px; height: 777px;
    background: var(--paper); font-family: "EB Garamond", Georgia, serif;
  }
  .top-band { position: absolute; left: 0; top: 0; width: 100%; height: 8px; background: var(--navy); }
  .brand-dot {
    position: absolute; top: 15px; left: 288px; width: 24px; height: 24px;
    border-radius: 50%; background: var(--navy);
  }
  .brand-name, .brand-sub, .tagline {
    position: absolute; left: 0; width: 100%; text-align: center; color: var(--navy); white-space: nowrap;
  }
  .brand-name { top: 40px; font-size: 12px; line-height: 14px; letter-spacing: 3.5px; padding-left: 3.5px; }
  .brand-sub { top: 51px; font-size: 9px; line-height: 10px; }
  .tagline { top: 69px; font-size: 12.5px; line-height: 14px; font-weight: 500; letter-spacing: 0.3px; }
  .rule {
    position: absolute; left: 78px; width: 447px; height: 2px;
    background: linear-gradient(90deg, var(--rule-fade), var(--navy) 50%, var(--rule-fade));
  }
  .rule-head { top: 90px; }
  .rule-foot { top: 731px; }
  .contact {
    position: absolute; top: 740px; left: 0; width: 100%; text-align: center;
    font-size: 12.5px; line-height: 18px; color: var(--footer-ink); word-spacing: 1px; white-space: nowrap;
  }
  .contact span + span { margin-left: 12px; }
  .footer-band { position: absolute; left: 0; bottom: 0; width: 100%; height: 19px; background: var(--footer-band); }
  .footer-band::after { content: ""; position: absolute; left: 402px; top: 0; width: 2px; height: 100%; background: var(--paper); }
</style>
</head>
<body>
  <div class="canvas">
    <div class="sheet">
      <div class="top-band"></div>
      <header class="brand">
        <span class="brand-dot"></span>
        <span class="brand-name">MERIDIAN</span>
        <span class="brand-sub">Advisory Group LLC</span>
        <span class="tagline">WHERE PROGRESS BEGINS</span>
      </header>
      <div class="rule rule-head"></div>
      <div class="rule rule-foot"></div>
      <footer class="contact">
        <span>418 Alder Crest Road Santa Clara</span>
        <span>Tel: 1+ (555) 014-2000</span>
        <span>Fax: 1+ (555) 014-2200</span>
      </footer>
      <div class="footer-band"></div>
    </div>
  </div>
</body>
</html>
```